Web Site for Strategy and Technology Consulting Company

We are looking for a website design that engages potential customers to understand our services and contact us. In this contest, we are looking for a homepage design, but the winning designer will be favored for the design of some of the more complicated interior pages of the site. An additional contest (or contests) for these pages will be added soon.

PLATROM AND RESPONSIVE DESIGN
The site will be implemented in WordPress using the Elementor page builder.
We are looking for a design that will look good on phones are well as laptop browsers.

UPLOADED FILES INCLUDE:
1a A wireframe of the homepage we are looking for. The Uploaded PDF also includes a draft of the text proposed for the homepage. Designers are free to go beyond the wireframe, but all elements of the wireframe should be included.
1b A Word document with the draft text of the homepage.
2a-d The Norvalith logo. Two versions are included – a dark version which works well against a light background, and a light version which works well against a dark background.
3 The Norvalith color palette with HEX and RGB values. Designers are not limited to this palette, but colors should be complementary.
4 A draft of the homepage menu
5 Service sheets with information on the services we provide

MORE ABOUT NORVALITH
Norvalith is a consulting company focused on transforming businesses through software. Our tagline, “Transformation Delivered,” recognizes the gap business often have between business transformation and the software they end up with. By listening to our customers and understanding their vision and where they are, we help get our customers where they want to go.

We increase our capability by working with many consultants and partners, allowing us to provide our customers with the best people and the software that best suits them.

Industry/Entity Type

Consulting

Number of Pages Required

1 page

Font styles to use
Sans Serif

Requirements
Must have
• the content represented on the wireframe uploaded
Nice to have
• interactive features, such as roll-over icons that reveal additional information

```html
<!DOCTYPE html>
<html lang="en">
<head>
<meta charset="utf-8">
<title>Norvalith — Transformation Delivered</title>
<link href="https://fonts.googleapis.com/css2?family=Poppins:wght@400;500;600;700&display=swap" rel="stylesheet">
<style>
:root{
  --night:#050d1c;
  --navy:#0a1a33;
  --blue:#1f5ea8;
  --blue-dark:#16427c;
  --cta:#1565e0;
  --yellow:#f2d026;
  --gold:#e7c437;
  --lavender:#a9b4f5;
  --white:#ffffff;
  --muted:#c9d3e4;
}
*{box-sizing:border-box;margin:0;padding:0}
html,body{width:1200px;height:3859px;overflow:hidden}
body{background:var(--night);color:var(--white);font-family:'Poppins',sans-serif;position:relative}
.abs{position:absolute}
a{color:inherit;text-decoration:none}

/* header */
.site-header{position:absolute;left:0;top:0;width:1200px;height:95px;background:linear-gradient(#0b0b0b,#16181c);border-bottom:2px solid #2a2d33}
.brand{position:absolute;left:121px;top:20px;font-size:38px;font-weight:500;color:#c8ccd4;letter-spacing:.5px}
.nav{position:absolute;left:385px;top:33px;display:flex;gap:54px;font-size:15px;font-weight:500}
.nav li{list-style:none;display:flex;align-items:center;gap:10px}
.nav .active:before{content:"";width:11px;height:11px;background:var(--yellow)}
.contact-btn{position:absolute;left:930px;top:24px;width:150px;height:38px;border-radius:19px;background:var(--gold);color:#111;font-size:15px;font-weight:500;display:flex;align-items:center;justify-content:center}

/* hero */
.hero{position:absolute;left:0;top:95px;width:1200px;height:534px;background:radial-gradient(ellipse at 85% 95%,#5a1240 0%,transparent 45%),linear-gradient(135deg,#0a1f3e 0%,#071530 45%,#0d1230 100%)}
.hero-photo{position:absolute;left:0;top:60px;width:690px;height:474px;background:linear-gradient(180deg,rgba(40,50,70,.2),rgba(30,32,40,.9) 55%,#1a1c22)}
.hero-title{position:absolute;left:692px;top:100px;font-size:46px;font-weight:600;line-height:52px}
.hero-title .y{color:var(--yellow)}
.hero-text{position:absolute;left:697px;top:222px;width:340px;font-size:16.5px;line-height:29px;color:#e8ecf4}
.btn{border-radius:18px;background:var(--cta);color:#fff;font-size:15px;font-weight:500;display:flex;align-items:center;justify-content:center}
.scroll-pill{position:absolute;left:632px;top:599px;width:30px;height:63px;border-radius:15px;background:var(--yellow)}
.scroll-pill:after{content:"";position:absolute;left:12px;top:22px;width:6px;height:14px;border-radius:3px;background:#fff}

/* tech */
.tech{position:absolute;left:0;top:629px;width:1200px;height:470px;background:linear-gradient(180deg,#0a1730 0%,#0b1e3d 60%,#0c2347 100%)}
.tech-photo{position:absolute;left:130px;top:40px;width:600px;height:380px;background:radial-gradient(ellipse at 50% 50%,rgba(60,80,120,.55),rgba(12,30,60,0) 70%)}
.tech-title{position:absolute;left:590px;top:112px;font-size:32px;font-weight:600;line-height:40px}
.tech-title .y{color:var(--yellow);font-size:34px}
.tech-text{position:absolute;left:592px;top:212px;width:500px;font-size:15px;line-height:26px;color:#e3e8f1}

/* differentiators */
.diff{position:absolute;left:0;top:1060px;width:1200px;height:680px;background:linear-gradient(180deg,#0c2347 0%,#0a1e3e 50%,var(--night) 100%)}
.diff-title{position:absolute;left:0;width:1200px;top:22px;text-align:center;font-size:38px;font-weight:600}
.diff-frame{position:absolute;left:386px;top:189px;width:439px;height:417px;border:7px solid var(--yellow);border-radius:26px;overflow:hidden;background:linear-gradient(180deg,#1d4f90,#0a1e3e)}
.diff-art{position:absolute;left:0;top:0;width:100%;height:100%;background:radial-gradient(ellipse at 50% 45%,rgba(150,140,125,.45) 0%,rgba(29,79,144,0) 65%)}
.icon-box{position:absolute;width:62px;height:54px;background:var(--yellow);border:5px solid var(--blue);display:flex;align-items:center;justify-content:center}
.diff-label{position:absolute;font-size:19px;line-height:24px}
.diff-label.left{text-align:right;width:240px}

/* resources */
.res-deco{position:absolute;left:386px;top:1771px;width:128px;height:116px;background:var(--gold);border-radius:8px}
.res-deco2{position:absolute;left:354px;top:1792px;width:56px;height:52px;background:var(--blue);border-radius:10px}
.res-photo{position:absolute;left:123px;top:1806px;width:347px;height:568px;border:6px solid var(--blue-dark);border-radius:10px;background:linear-gradient(160deg,#d8d8d6 0%,#a89a88 55%,#6b4e35 100%)}
.sq{position:absolute}
.res-title{position:absolute;left:547px;top:1866px;font-size:32px;font-weight:600;color:var(--gold)}
.res-text{position:absolute;left:547px;top:1910px;width:540px;font-size:16.5px;line-height:29px}
.res-item{position:absolute;left:547px;width:560px;display:flex;gap:22px;font-size:16px;line-height:25px}
.res-sep{position:absolute;left:547px;top:2117px;width:561px;height:1px;background:#7a8699}

/* testimonials */
.testi-title{position:absolute;left:0;width:1180px;top:2470px;text-align:center;font-size:34px;font-weight:600;color:var(--gold)}
.quote-card{position:absolute;top:2565px;width:460px;height:326px;border:6px solid var(--blue-dark);border-radius:6px;padding:58px 48px 0;text-align:center;font-size:15px;line-height:25.5px}
.quote-card.yellow{background:var(--yellow);color:#1a1a1a}
.quote-card.blue{background:var(--blue);color:#fff}
.qmark{font-size:54px;font-weight:700;line-height:30px;position:absolute}
.author{font-weight:600;font-size:15px;margin-top:2px}
.role{font-size:12.5px;letter-spacing:1px;line-height:14px}
.avatar{position:absolute;top:2482px;width:134px;height:134px;border-radius:50%;border:6px solid var(--blue-dark)}
.arrow-btn{position:absolute;width:46px;height:44px;display:flex;align-items:center;justify-content:center}

/* feature cards */
.rule{position:absolute;left:120px;top:3020px;width:960px;height:1px;background:#4a5568}
.feature{position:absolute;top:3044px;height:333px;border:6px solid var(--blue-dark);border-radius:6px;text-align:center;padding-top:38px}
.feature.yellow{background:var(--yellow);color:#151515}
.feature.blue{background:var(--blue);color:#fff}
.feat-icon{width:92px;height:92px;border-radius:50%;background:#fff;border:5px solid var(--blue-dark);margin:0 auto 18px;display:flex;align-items:center;justify-content:center}
.feature h3{font-size:14.5px;font-weight:600;margin-bottom:8px}
.feature p{font-size:11px;line-height:19px;padding:0 26px}
.feature .more{display:inline-block;margin-top:18px;font-size:13px;font-weight:600;letter-spacing:1px;text-decoration:underline}

/* footer */
.footer{position:absolute;left:0;top:3453px;width:1200px;height:406px;background:var(--night)}
.foot-brand{position:absolute;left:121px;top:145px;font-size:36px;font-weight:500;color:#c8ccd4}
.foot-col{position:absolute;top:84px}
.foot-col .bar{width:76px;height:5px;background:linear-gradient(90deg,var(--blue) 50%,var(--yellow) 50%);margin-bottom:10px}
.foot-col h4{font-size:17px;font-weight:500;color:#5f9cf0;margin-bottom:14px}
.foot-col li{list-style:none;font-size:13.5px;line-height:33px;display:flex;align-items:center;gap:12px}
.foot-col li:before{content:"";width:9px;height:9px;background:var(--yellow);flex:none}
.foot-col.services li{line-height:29px}
.loc-row{display:flex;gap:16px;font-size:14px;line-height:21px;margin-bottom:30px}
.foot-rule{position:absolute;left:120px;top:317px;width:960px;height:1px;background:#2c3645}
.copyright{position:absolute;left:0;width:1200px;top:332px;text-align:center;font-size:16px}
.copyright span{color:var(--gold)}
.to-top{position:absolute;left:1035px;top:326px;width:42px;height:42px;border-radius:50%;background:var(--gold);display:flex;align-items:center;justify-content:center}
</style>
</head>
<body>

<header class="site-header">
  <div class="brand">Norvalith</div>
  <ul class="nav">
    <li class="active">Home</li><li>About Us</li><li>Service</li><li>Insights</li><li>Join Us</li>
  </ul>
  <a class="contact-btn">Contact Us</a>
</header>

<section class="hero">
  <div class="hero-photo" role="img" aria-label="Team of four business professionals in suits standing together"></div>
  <div class="sq" style="left:1046px;top:85px;width:34px;height:34px;background:var(--blue)"></div>
  <div class="sq" style="left:1086px;top:124px;width:35px;height:34px;background:var(--lavender)"></div>
  <div class="sq" style="left:1046px;top:136px;width:22px;height:22px;background:var(--yellow)"></div>
  <div class="sq" style="left:1010px;top:158px;width:22px;height:23px;background:var(--lavender)"></div>
  <h1 class="hero-title"><span class="y">Transformation</span><br>Delivered</h1>
  <p class="hero-text">We do more for our customers than implement software. We start by understanding their strategy, or we help them build their strategy. We listen.</p>
  <a class="btn abs" style="left:690px;top:381px;width:150px;height:36px">Our Story</a>
</section>
<div class="scroll-pill"></div>

<section class="tech">
  <div class="tech-photo" role="img" aria-label="Team meeting around a table with laptops"></div>
  <h2 class="tech-title">Transformation<br><span class="y">Supported by Technology</span></h2>
  <p class="tech-text">Lorem Ipsum is simply dummy text of the printing and typesetting industry. Lorem Ipsum has been the industry's standard dummy text ever since the 1500s, when an unknown printer took a galley of type and scrambled it to make a type specimen book. It has survived not only five centuries, but also the leap into electronic</p>
</section>

<section class="diff">
  <h2 class="diff-title">Differentiators around our services</h2>
  <a class="btn abs" style="left:503px;top:101px;width:192px;height:44px;border-radius:22px">How We Work</a>
  <div class="diff-frame">
    <div class="diff-art" role="img" aria-label="Photo collage of business scenes arranged as a large letter"></div>
  </div>
  <div class="diff-label left" style="left:100px;top:280px">Transformation<br>Planning</div>
  <div class="diff-label left" style="left:98px;top:390px">CRM Solutions</div>
  <div class="diff-label left" style="left:97px;top:491px">ERP Solutions</div>
  <div class="diff-label" style="left:875px;top:276px">Data and Business<br>intelligence</div>
  <div class="diff-label" style="left:875px;top:390px">Amplify</div>
  <div class="icon-box" style="left:358px;top:272px"><svg width="26" height="26" viewBox="0 0 26 26" fill="none" stroke="#1f4f8a" stroke-width="1.6"><circle cx="13" cy="13" r="4"/><circle cx="13" cy="3" r="2"/><circle cx="13" cy="23" r="2"/><circle cx="3" cy="13" r="2"/><circle cx="23" cy="13" r="2"/></svg></div>
  <div class="icon-box" style="left:358px;top:378px"><svg width="28" height="26" viewBox="0 0 28 26" fill="none" stroke="#1f4f8a" stroke-width="1.6"><rect x="2" y="3" width="24" height="16"/><path d="M8 15v-4M12 15V8M16 15v-6M20 15V6M10 23h8M14 19v4"/></svg></div>
  <div class="icon-box" style="left:358px;top:478px"><svg width="28" height="26" viewBox="0 0 28 26" fill="none" stroke="#1f4f8a" stroke-width="1.6"><rect x="3" y="8" width="22" height="15"/><path d="M7 18l5-5 4 3 6-6M10 3h8"/></svg></div>
  <div class="icon-box" style="left:786px;top:272px"><svg width="28" height="26" viewBox="0 0 28 26" fill="none" stroke="#1f4f8a" stroke-width="1.6"><rect x="5" y="9" width="18" height="12"/><path d="M14 3v6M9 15h10M3 23h22"/><circle cx="14" cy="3" r="1.5"/></svg></div>
  <div class="icon-box" style="left:790px;top:380px"><svg width="26" height="26" viewBox="0 0 26 26" fill="none" stroke="#1f2a3a" stroke-width="2.2"><path d="M3 9V3h6M17 3h6v6M23 17v6h-6M9 23H3v-6"/></svg></div>
</section>

<div class="res-deco2"></div>
<div class="res-photo" role="img" aria-label="Two colleagues reviewing a tablet together"></div>
<div class="res-deco"></div>
<div class="sq" style="left:497px;top:2252px;width:19px;height:19px;background:var(--gold)"></div>
<div class="sq" style="left:463px;top:2275px;width:29px;height:29px;background:var(--blue)"></div>
<div class="sq" style="left:485px;top:2318px;width:17px;height:17px;background:var(--lavender)"></div>
<div class="sq" style="left:376px;top:2317px;width:29px;height:29px;background:var(--lavender)"></div>
<div class="sq" style="left:437px;top:2305px;width:26px;height:26px;background:var(--blue-dark)"></div>
<div class="sq" style="left:343px;top:2357px;width:26px;height:24px;background:var(--blue)"></div>
<div class="sq" style="left:411px;top:2355px;width:29px;height:29px;background:var(--gold)"></div>
<div class="sq" style="left:311px;top:2386px;width:29px;height:29px;background:var(--lavender)"></div>
<div class="sq" style="left:369px;top:2386px;width:36px;height:36px;border:5px solid var(--lavender);background:#000"></div>
<div class="sq" style="left:431px;top:2389px;width:22px;height:22px;background:var(--blue)"></div>

<h2 class="res-title">Resources</h2>
<p class="res-text">The world has changed in the past twenty years. The people you need might not all work for one company. Our clients want the best resources, available quickly. That's why, in addition to our team of experts, we partner with:</p>
<div class="res-item" style="top:2054px"><svg width="28" height="30" viewBox="0 0 28 30"><path d="M2 16l9 10L26 2" fill="none" stroke="var(--gold)" stroke-width="5"/></svg><span>A large network of expert consultants who are the best at what they do,</span></div>
<div class="res-sep"></div>
<div class="res-item" style="top:2127px"><svg width="28" height="30" viewBox="0 0 28 30"><path d="M2 16l9 10L26 2" fill="none" stroke="var(--gold)" stroke-width="5"/></svg><span>Service providers all over the world to provide the resources and value that are right for you, available 24 x 7.</span></div>
<p class="res-text" style="top:2198px;font-size:16px;line-height:24px">People are invariably at the center of our customer's success. Find out how we can add our experts to yours.</p>
<a class="btn abs" style="left:548px;top:2265px;width:160px;height:46px;border-radius:23px">Our Team</a>

<h2 class="testi-title">Testimonials</h2>
<div class="arrow-btn" style="left:60px;top:2702px;background:#fff"><svg width="14" height="18" viewBox="0 0 14 18"><path d="M10 2L3 9l7 7" fill="none" stroke="#111" stroke-width="3"/></svg></div>
<div class="arrow-btn" style="left:1105px;top:2702px;background:#fff"><svg width="14" height="18" viewBox="0 0 14 18"><path d="M4 2l7 7-7 7" fill="none" stroke="#111" stroke-width="3"/></svg></div>
<div class="quote-card yellow" style="left:126px">
  <span class="qmark" style="left:40px;top:46px">“</span>
  <p>Lorem Ipsum is simply dummy text of the printing and typesetting industry. Lorem Ipsum has been the industry's standard dummy text ever since the 1500s, when an unknown printer took a galley of type and scrambled it to make a type specimen book. It has survived not only five centuries,</p>
  <span class="qmark" style="left:296px;top:236px">”</span>
  <p class="author">Mara Ellison</p><p class="role">(Business Developer)</p>
</div>
<div class="quote-card blue" style="left:622px">
  <span class="qmark" style="left:40px;top:46px;color:#7fb0f5">“</span>
  <p>Lorem Ipsum is simply dummy text of the printing and typesetting industry. Lorem Ipsum has been the industry's standard dummy text ever since the 1500s, when an unknown printer took a galley of type and scrambled it to make a type specimen book. It has survived not only five centuries,</p>
  <span class="qmark" style="left:296px;top:236px;color:#7fb0f5">”</span>
  <p class="author">Mara Ellison</p><p class="role">(Business Developer)</p>
</div>
<div class="avatar" style="left:287px;background:linear-gradient(160deg,#e8e2d8,#b8875a)" role="img" aria-label="Portrait of a smiling client"></div>
<div class="avatar" style="left:783px;background:linear-gradient(160deg,#6b7f99,#1f5ea8)" role="img" aria-label="Portrait of a smiling client"></div>

<div class="arrow-btn" style="left:972px;top:2963px;background:var(--yellow)"><svg width="14" height="18" viewBox="0 0 14 18"><path d="M10 2L3 9l7 7" fill="none" stroke="#111" stroke-width="3"/></svg></div>
<div class="arrow-btn" style="left:1034px;top:2963px;background:var(--yellow)"><svg width="14" height="18" viewBox="0 0 14 18"><path d="M4 2l7 7-7 7" fill="none" stroke="#111" stroke-width="3"/></svg></div>
<div class="rule"></div>

<div class="feature yellow" style="left:120px;width:225px">
  <div class="feat-icon"><svg width="54" height="54" viewBox="0 0 54 54" fill="none" stroke="var(--blue-dark)" stroke-width="3"><path d="M16 36a10 10 0 0 1 2-20 13 13 0 0 1 24 4 8 8 0 0 1-2 16"/><path d="M27 44V24M20 31l7-7 7 7"/></svg></div>
  <h3>Been the industry's</h3><p>Dummy text of the printing and typesetting industry. Lorem Ipsum has been the industry's standard</p><a class="more">READ MORE</a>
</div>
<div class="feature blue" style="left:362px;width:221px">
  <div class="feat-icon"><svg width="54" height="54" viewBox="0 0 54 54" fill="none" stroke="var(--blue-dark)" stroke-width="3"><circle cx="27" cy="27" r="17"/><circle cx="27" cy="27" r="7"/><path d="M27 6v8M27 40v8M6 27h8M40 27h8"/></svg></div>
  <h3>Been the industry's</h3><p>Dummy text of the printing and typesetting industry. Lorem Ipsum has been the industry's standard</p><a class="more">READ MORE</a>
</div>
<div class="feature blue" style="left:605px;width:226px">
  <div class="feat-icon"><svg width="54" height="54" viewBox="0 0 54 54" fill="var(--blue-dark)"><circle cx="27" cy="27" r="20"/><circle cx="27" cy="27" r="7" fill="#fff"/><path d="M27 14v26" stroke="#fff" stroke-width="3"/></svg></div>
  <h3>Been the industry's</h3><p>Dummy text of the printing and typesetting industry. Lorem Ipsum has been the industry's standard</p><a class="more">READ MORE</a>
</div>
<div class="feature blue" style="left:849px;width:228px">
  <div class="feat-icon" style="background:var(--blue-dark);border-color:#fff"><svg width="54" height="54" viewBox="0 0 54 54" fill="none" stroke="#fff" stroke-width="4"><path d="M10 22a24 24 0 0 1 34 0M16 29a15 15 0 0 1 22 0M22 35a6 6 0 0 1 10 0"/><circle cx="27" cy="41" r="2.5" fill="#fff"/></svg></div>
  <h3>Been the industry's</h3><p>Dummy text of the printing and typesetting industry. Lorem Ipsum has been the industry's standard</p><a class="more">READ MORE</a>
</div>

<footer class="footer">
  <div class="foot-brand">Norvalith</div>
  <div class="foot-col" style="left:418px">
    <div class="bar"></div><h4>Sitemap</h4>
    <ul><li>Home</li><li>About Us</li><li>Service</li><li>Insights</li><li>Join Us</li></ul>
  </div>
  <div class="foot-col" style="left:611px">
    <div class="bar"></div><h4>Location</h4>
    <div class="loc-row"><svg width="22" height="24" viewBox="0 0 22 24" fill="none" stroke="var(--gold)" stroke-width="1.6"><path d="M11 22s-7-7-7-12a7 7 0 0 1 14 0c0 5-7 12-7 12z"/><circle cx="11" cy="10" r="2.5"/></svg><span>418 Harbor Lane Suite 210,<br>Fairview, MN 55012</span></div>
    <div class="loc-row"><svg width="22" height="22" viewBox="0 0 22 22" fill="none" stroke="var(--gold)" stroke-width="1.6"><path d="M4 2h4l2 5-3 2a11 11 0 0 0 6 6l2-3 5 2v4a2 2 0 0 1-2 2A18 18 0 0 1 2 4a2 2 0 0 1 2-2z"/></svg><span>(555) 014-2291</span></div>
    <div class="loc-row"><svg width="22" height="18" viewBox="0 0 22 18" fill="none" stroke="var(--gold)" stroke-width="1.6"><rect x="1" y="2" width="20" height="14"/><path d="M1 2l10 8 10-8"/></svg><span>hello@norvalith.com</span></div>
  </div>
  <div class="foot-col services" style="left:909px">
    <div class="bar"></div><h4>Services</h4>
    <ul><li>When an unknown</li><li>Printer took a galley</li><li>Type and scrambled</li><li>To make a type</li><li>Specimen book. It Has</li><li>survived</li></ul>
  </div>
  <div class="foot-rule"></div>
  <p class="copyright">Copyright © 2023 <span>Norvalith</span></p>
  <a class="to-top"><svg width="14" height="10" viewBox="0 0 14 10"><path d="M2 8l5-5 5 5" fill="none" stroke="#fff" stroke-width="1.6"/></svg></a>
</footer>

</body>
</html>
```